Standard logo business card

We are seeking a solid, somewhat understated professional design. We are a tech company. We like fonts similar to Aptifer Slab. Front side will be white with the contact information and a small version of our primary (Light background) logo.

(We have three people so we will have three names and titles)

Back side will hold our reverse logo on dark background along with the tagline:

"Intelligent annotation solutions for complex data"

Target Market(s)

Professionals, Tech

Industry/Entity Type

Business

Contact Information for Business Card

Name
Title

Phone
Email
City, State
Website

[We will email leading designer specific contact information)

Font styles to use
Serif

Requirements
Must have
• Colors are:
• Orange RGB 245,92,23
• Blue RGB 3,34,56
Nice to have
• We like a split with the Name and Title on the right and then contact details (below) on the left.

```html
<!DOCTYPE html>
<html lang="en">
<head>
<meta charset="utf-8">
<title>Norvanta Business Card</title>
<link href="https://fonts.googleapis.com/css2?family=Bitter:wght@400;600;700&display=swap" rel="stylesheet">
<style>
  :root {
    --orange: rgb(245, 92, 23);
    --frame-orange: #f05f24;
    --navy: rgb(3, 34, 56);
    --navy-card: #072238;
    --white: #ffffff;
  }
  * { margin: 0; padding: 0; box-sizing: border-box; }
  html, body {
    width: 1000px;
    height: 1200px;
    overflow: hidden;
    background: var(--frame-orange);
    font-family: "Bitter", Georgia, serif;
  }
  .canvas {
    position: relative;
    width: 1000px;
    height: 1200px;
  }
  .card {
    position: absolute;
    left: 81px;
    width: 838px;
    overflow: hidden;
  }
  .card-front {
    top: 51px;
    height: 549px;
    background: var(--white);
    color: var(--navy);
  }
  .card-back {
    top: 600px;
    height: 550px;
    background: var(--navy-card);
    color: var(--white);
  }
  .brand {
    position: absolute;
    display: flex;
    align-items: center;
    font-weight: 700;
    letter-spacing: -0.02em;
    white-space: nowrap;
  }
  .brand-square {
    background: var(--orange);
    border-radius: 3px;
    flex: none;
  }
  .brand-small {
    left: 424px;
    top: 28px;
    font-size: 40px;
    color: var(--navy);
    gap: 10px;
  }
  .brand-small .brand-square { width: 36px; height: 36px; }
  .brand-large {
    left: 167px;
    top: 222px;
    font-size: 92px;
    color: var(--white);
    gap: 22px;
  }
  .brand-large .brand-square { width: 84px; height: 84px; border-radius: 5px; }
  .person {
    position: absolute;
    left: 478px;
    top: 312px;
  }
  .person-name {
    font-size: 34px;
    font-weight: 400;
    line-height: 1.1;
  }
  .person-title {
    font-size: 18px;
    letter-spacing: 0.02em;
    margin-top: 2px;
  }
  .contact {
    position: absolute;
    right: 360px;
    top: 438px;
    text-align: right;
    list-style: none;
    font-size: 16px;
    line-height: 21px;
    letter-spacing: 0.02em;
  }
  .contact-label {
    color: var(--orange);
    font-size: 12.5px;
    margin-right: 3px;
  }
  .tagline {
    position: absolute;
    left: 0;
    right: 0;
    top: 473px;
    text-align: center;
    font-size: 19px;
    letter-spacing: 0.04em;
    text-transform: uppercase;
  }
</style>
</head>
<body>
<main class="canvas">
  <section class="card card-front">
    <div class="brand brand-small"><span class="brand-square"></span>norvanta</div>
    <div class="person">
      <h1 class="person-name">Daniel Harper</h1>
      <p class="person-title">TITLE</p>
    </div>
    <ul class="contact">
      <li><span class="contact-label">phone</span>12345 6789</li>
      <li><span class="contact-label">email</span>dharper@email.com</li>
      <li><span class="contact-label">address</span>City, State</li>
      <li><span class="contact-label">web</span>www.website.com</li>
    </ul>
  </section>
  <section class="card card-back">
    <div class="brand brand-large"><span class="brand-square"></span>norvanta</div>
    <p class="tagline">Intelligent annotation solutions for complex data</p>
  </section>
</main>
</body>
</html>
```